Business Card Design Project

This is the first time we use our new logo. We need a business card that we can use both on our institutional corporate relationships and also that works for our staff that deals with consumers directly.

VELUNDA is a new company dedicated to empower consumers and to provide them with the best choices for specialized health care using the latest telemedicine technology (medicine at a distance via videoconference).

We want to print this cards in high quality materials and process. We will like designs that allow us to use UV spot varnish and other techniques that will differentiate us.

We are including Two different versions of Color logos. In addition we are including white over black background logos. Those can be used replacing the black for a color.

Please note this is the first time we will be creating any corporate materials with our new logo and colors.

Target Market(s)

34+ consumers of medium high and high socioeconomic levels.

Industry/Entity Type

Health

Requirements
Must have
• Our logo on its original colors
Should not have
• Any other graphical element or design that is not our logo

```html
<!DOCTYPE html>
<html lang="en">
<head>
<meta charset="utf-8">
<title>Velunda Business Card</title>
<link rel="stylesheet" href="https://fonts.googleapis.com/css2?family=Marcellus+SC&display=swap">
<style>
  :root {
    --page-bg: #e9ecef;
    --card-bg: #ffffff;
    --card-edge: #eef1f4;
    --ink-navy: #23456b;
    --ink-slate: #2f3f4f;
    --ink-grey: #4a5560;
    --brand-blue: #2b8fd0;
  }
  * { margin: 0; padding: 0; box-sizing: border-box; }
  html, body {
    width: 1200px; height: 750px; overflow: hidden;
    background: var(--page-bg);
  }
  .canvas {
    position: relative; width: 1200px; height: 750px;
    font-family: "Marcellus SC", "Times New Roman", serif;
  }
  .card {
    position: absolute; left: 275px; width: 642px; height: 345px;
    border-radius: 24px; overflow: hidden;
    background: radial-gradient(circle at 35% 40%, var(--card-bg) 55%, var(--card-edge) 100%);
    box-shadow: 0 6px 18px rgba(0,0,0,0.18);
  }
  .card--front { top: 18px; }
  .card--back { top: 396px; }

  .person { position: absolute; left: 28px; top: 84px; width: 330px; }
  .person__name {
    font-size: 52px; font-weight: 400; color: var(--ink-navy);
    letter-spacing: 1px; line-height: 1; white-space: nowrap;
  }
  .person__role {
    text-align: right; font-size: 24px; color: var(--ink-slate);
    line-height: 1; margin-top: 8px;
  }
  .contact {
    position: absolute; left: 28px; top: 186px; list-style: none;
    font-size: 23px; line-height: 30px; white-space: nowrap;
  }
  .contact__label { color: var(--ink-slate); }
  .contact__value { color: var(--ink-grey); }

  .brand {
    position: absolute; left: 130px; top: 78px; height: 100px;
    display: flex; align-items: center; gap: 28px;
  }
  .brand__dot {
    width: 90px; height: 90px; border-radius: 50%;
    background: var(--brand-blue);
  }
  .brand__name {
    font-size: 60px; color: var(--ink-navy); letter-spacing: 2px; line-height: 1;
  }
</style>
</head>
<body>
<main class="canvas">
  <section class="card card--front">
    <div class="person">
      <h1 class="person__name">Daren Kostel</h1>
      <p class="person__role">President</p>
    </div>
    <ul class="contact">
      <li><span class="contact__label">Adress:</span> <span class="contact__value">Marin Velkov</span></li>
      <li><span class="contact__label">Mobile:</span> <span class="contact__value">38971 586 204</span></li>
      <li><span class="contact__label">E-mail:</span> <span class="contact__value">darenkostel@mail.com</span></li>
      <li><span class="contact__label">Fax:</span> <span class="contact__value">38972 417 650</span></li>
      <li><span class="contact__label">Website:</span> <span class="contact__value">www.velunda.com</span></li>
    </ul>
  </section>

  <section class="card card--back">
    <div class="brand">
      <span class="brand__dot"></span>
      <span class="brand__name">VELUNDA</span>
    </div>
  </section>
</main>
</body>
</html>
```